Social Media App Needs PPT Template

We need a PowerPoint template for a new social media company based in the DC area called "Clear Ledger." We provide an interactive digital platform for executives to share actionable advice. We would like to see designs that use our orange logo color as an accent, but are mainly grey, white, and black. The final design should communicate clean, chic, modern, and professional.

Target Market(s)

Executives

Industry/Entity Type

Information Technology

Font styles to use
Sans Serif

Colors
f78f20
fbe7d2
ffffff
000000
e8e8e8
757575

Requirements
Must have
• My project must have title page and many options for the body of the ppt (graphs, tables, etc). It also needs to be easy to modify. I must have someone who is experienced in creating powerpoint templates.
Nice to have
• It would be nice to have a very modern and clean design that includes the logo on every page, but still leaves a lot of room for the content of the slide
Should not have
• My design project should not look to busy.

```html
<!DOCTYPE html>
<html lang="en">
<head>
<meta charset="utf-8">
<title>Clear Ledger — Presentation Template</title>
<link href="https://fonts.googleapis.com/css2?family=Montserrat:wght@500;600;700&family=Open+Sans:wght@400;600;700&display=swap" rel="stylesheet">
<style>
:root{
  --orange:#f78f20;
  --peach:#fbe7d2;
  --yellow:#f9b81b;
  --white:#ffffff;
  --black:#000000;
  --light:#e8e8e8;
  --mid:#a9a9a9;
  --grey:#757575;
  --dark:#3d3f44;
  --ink:#2b2b2b;
}
*{margin:0;padding:0;box-sizing:border-box}
html,body{width:822px;height:1200px;overflow:hidden;background:var(--white)}
.deck{position:relative;width:822px;height:1200px}
.slide{position:absolute;width:255px;height:144px;background:linear-gradient(160deg,#f6f6f6,#ebebeb);overflow:hidden;box-shadow:0 1px 3px rgba(0,0,0,.18)}
.c1{left:13px}.c2{left:284px}.c3{left:553px}
.r1{top:11px}.r2{top:160px}.r3{top:309px}.r4{top:458px}.r5{top:607px}.r6{top:756px}.r7{top:905px}.r8{top:1054px}
.slide-head{position:absolute;left:9px;top:5px;z-index:2}
.slide-head::before{content:"";display:block;width:12px;height:1.5px;background:var(--orange);margin-bottom:1px}
.slide-head h2{font:600 8px/1 'Montserrat',sans-serif;color:#555;letter-spacing:.2px}
.slide-head p{font:700 3.6px/1.4 'Open Sans',sans-serif;color:#666}
.brand-foot{position:absolute;left:8px;bottom:4px;display:flex;align-items:center;gap:2px;font:700 3.6px/1 'Montserrat',sans-serif;color:var(--ink);z-index:2}
.brand-foot i{display:block;width:4px;height:4px;border-radius:50%;background:var(--orange)}
.page-no{position:absolute;right:6px;bottom:4px;background:var(--dark);color:var(--white);font:700 3.2px/1 'Open Sans',sans-serif;padding:1.2px 2.5px;border-radius:3px;z-index:2}
.art{position:absolute;inset:0;width:255px;height:144px}
svg text{font-family:'Open Sans',sans-serif}
.t{font-size:2.6px;fill:#9a9a9a}
.lb{font-size:3.2px;font-weight:700;fill:#444}
.lbo{font-size:3.2px;font-weight:700;fill:var(--orange)}
.num{font-family:'Montserrat',sans-serif;font-weight:600}
.photo{position:absolute}
.title-block{position:absolute;left:0;right:0;top:75px;bottom:0;display:flex;align-items:center;justify-content:center;gap:22px}
.title-brand{display:flex;align-items:center;gap:3px;font:700 8px/1 'Montserrat',sans-serif;color:var(--ink)}
.title-brand i{display:block;width:10px;height:10px;border-radius:50%;background:var(--orange)}
.title-text h1{font:600 12px/1.1 'Montserrat',sans-serif;color:var(--orange)}
.title-text p{font:700 5px/1.5 'Open Sans',sans-serif;color:#555}
.thanks{background:var(--orange)}
.thanks h2{position:absolute;left:17px;top:70px;font:700 8.6px/1 'Montserrat',sans-serif;color:var(--white)}
</style>
</head>
<body>
<main class="deck">

<!-- Title A -->
<section class="slide c1 r1">
  <div class="photo" style="left:0;top:0;width:255px;height:75px;background:linear-gradient(180deg,#d7e6f4,#c6d8ea)" role="img" aria-label="Flat illustration of a desk seen from above with laptop, documents and hands typing"></div>
  <div class="title-block">
    <div class="title-brand"><i></i>Clear Ledger</div>
    <div class="title-text"><h1>Presentation Title</h1><p>Subheading goes here</p></div>
  </div>
</section>

<!-- Title B -->
<section class="slide c2 r1">
  <div class="photo" style="left:0;top:0;width:255px;height:75px;background:linear-gradient(120deg,#8e969e,#d9dde1 60%,#b8bfc5)" role="img" aria-label="Photo of hands working on a laptop showing charts"></div>
  <div class="title-block">
    <div class="title-brand"><i></i>Clear Ledger</div>
    <div class="title-text"><h1>Presentation Title</h1><p>Subheading goes here</p></div>
  </div>
</section>

<!-- Image with text panel -->
<section class="slide c3 r1">
  <header class="slide-head"><h2>MAIN HEADING</h2><p>Subheading goes here</p></header>
  <div class="photo" style="left:0;top:39px;width:125px;height:54px;background:linear-gradient(120deg,#2e3438,#5a6166)" role="img" aria-label="Photo of an open book on a desk"></div>
  <svg class="art" viewBox="0 0 255 144">
    <rect x="125" y="39" width="130" height="54" fill="#6e6e6e"/>
    <circle cx="126" cy="66" r="5" fill="var(--orange)"/>
    <text x="144" y="58" style="font-size:7px;font-weight:600;fill:#fff">Lorem ipsum</text>
    <text x="144" y="64" class="t" style="fill:#e0e0e0">Add a short note about this</text>
    <text x="144" y="68" class="t" style="fill:#e0e0e0">picture and the idea it shows</text>
    <text x="144" y="72" class="t" style="fill:#e0e0e0">to the audience today.</text>
    <text x="30" y="103" class="t">Write a short paragraph here that explains the main point of this slide in a clear way.</text>
    <text x="30" y="107" class="t">Keep it brief, use plain words and leave room around the text so it reads well.</text>
    <text x="30" y="111" class="t">A second line can add a detail or a simple example.</text>
  </svg>
  <div class="brand-foot"><i></i>Clear Ledger</div><span class="page-no">01</span>
</section>

<!-- Icon grid -->
<section class="slide c1 r2">
  <header class="slide-head"><h2>MAIN HEADING</h2><p>Subheading goes here</p></header>
  <svg class="art" viewBox="0 0 255 144">
    <line x1="127" y1="38" x2="127" y2="118" stroke="#d0d0d0" stroke-width=".6"/>
    <circle cx="112" cy="52" r="7" fill="var(--orange)"/>
    <path d="M108.5 53 L112 49.5 L115.5 53 M109.5 52.5 V55.5 H114.5 V52.5" stroke="#fff" stroke-width=".9" fill="none"/>
    <circle cx="112" cy="76" r="7" fill="var(--mid)"/>
    <path d="M112 79.5 C109 76 109 73 112 73 C115 73 115 76 112 79.5Z" stroke="#fff" stroke-width=".8" fill="none"/>
    <circle cx="112" cy="100" r="7" fill="var(--mid)"/>
    <rect x="108.5" y="97.5" width="7" height="5" rx=".8" stroke="#fff" stroke-width=".8" fill="none"/>
    <circle cx="143" cy="52" r="7" fill="var(--mid)"/>
    <path d="M140 49 H146 V51 C146 53.5 140 53.5 140 51Z M143 53 V55.5 M141 55.5 H145" stroke="#fff" stroke-width=".8" fill="none"/>
    <circle cx="143" cy="76" r="7" fill="var(--dark)"/>
    <path d="M140 79 L146 73 M146 73 L143.5 73.5 M146 73 L145.5 75.5" stroke="#fff" stroke-width=".9" fill="none"/>
    <circle cx="143" cy="100" r="7" fill="var(--orange)"/>
    <path d="M140 101 A3 3 0 1 1 146 101 M140 101 V102.5 M146 101 V102.5" stroke="#fff" stroke-width=".9" fill="none"/>
    <g text-anchor="end">
      <text x="100" y="50" class="lb">Lorem ipsum</text><text x="100" y="54" class="t">Add a short note about it.</text><text x="100" y="57.5" class="t">Keep the line brief.</text>
      <text x="100" y="74" class="lb">Lorem ipsum</text><text x="100" y="78" class="t">Add a short note about it.</text><text x="100" y="81.5" class="t">Keep the line brief.</text>
      <text x="100" y="98" class="lb">Lorem ipsum</text><text x="100" y="102" class="t">Add a short note about it.</text><text x="100" y="105.5" class="t">Keep the line brief.</text>
    </g>
    <text x="155" y="50" class="lb">Lorem ipsum</text><text x="155" y="54" class="t">Add a short note about it.</text><text x="155" y="57.5" class="t">Keep the line brief.</text>
    <text x="155" y="74" class="lb">Lorem ipsum</text><text x="155" y="78" class="t">Add a short note about it.</text><text x="155" y="81.5" class="t">Keep the line brief.</text>
    <text x="155" y="98" class="lb">Lorem ipsum</text><text x="155" y="102" class="t">Add a short note about it.</text><text x="155" y="105.5" class="t">Keep the line brief.</text>
  </svg>
  <div class="brand-foot"><i></i>Clear Ledger</div><span class="page-no">01</span>
</section>

<!-- Team -->
<section class="slide c2 r2">
  <header class="slide-head"><h2>MAIN HEADING</h2><p>Subheading goes here</p></header>
  <svg class="art" viewBox="0 0 255 144">
    <circle cx="48" cy="54" r="9" fill="#c9c9c9" role="img" aria-label="Team member portrait"/>
    <text x="63" y="48" class="lbo" style="font-size:2.8px">John Doe</text><text x="63" y="51" class="t" style="font-size:2px">Founder</text>
    <text x="63" y="55" class="t">Add a short note on role.</text><text x="63" y="58.5" class="t">Keep the line brief.</text>
    <circle cx="175" cy="54" r="9" fill="#c9c9c9" role="img" aria-label="Team member portrait"/>
    <text x="190" y="48" class="lbo" style="font-size:2.8px">Mary Doe</text><text x="190" y="51" class="t" style="font-size:2px">CEO</text>
    <text x="190" y="55" class="t">Add a short note on role.</text><text x="190" y="58.5" class="t">Keep the line brief.</text>
    <circle cx="48" cy="103" r="9" fill="#c9c9c9" role="img" aria-label="Team member portrait"/>
    <text x="63" y="97" class="lbo" style="font-size:2.8px">Mike Doe</text><text x="63" y="100" class="t" style="font-size:2px">Designer</text>
    <text x="63" y="104" class="t">Add a short note on role.</text><text x="63" y="107.5" class="t">Keep the line brief.</text>
    <circle cx="175" cy="103" r="9" fill="#c9c9c9" role="img" aria-label="Team member portrait"/>
    <text x="190" y="97" class="lbo" style="font-size:2.8px">Jenna Doe</text><text x="190" y="100" class="t" style="font-size:2px">Marketing</text>
    <text x="190" y="104" class="t">Add a short note on role.</text><text x="190" y="107.5" class="t">Keep the line brief.</text>
    <g fill="var(--orange)"><circle cx="44" cy="66" r="1.4"/><circle cx="48" cy="66" r="1.4" fill="var(--mid)"/><circle cx="52" cy="66" r="1.4" fill="var(--dark)"/>
      <circle cx="171" cy="66" r="1.4"/><circle cx="175" cy="66" r="1.4" fill="var(--mid)"/><circle cx="179" cy="66" r="1.4" fill="var(--dark)"/>
      <circle cx="44" cy="115" r="1.4"/><circle cx="48" cy="115" r="1.4" fill="var(--mid)"/><circle cx="52" cy="115" r="1.4" fill="var(--dark)"/>
      <circle cx="171" cy="115" r="1.4"/><circle cx="175" cy="115" r="1.4" fill="var(--mid)"/><circle cx="179" cy="115" r="1.4" fill="var(--dark)"/></g>
  </svg>
  <div class="brand-foot"><i></i>Clear Ledger</div><span class="page-no">01</span>
</section>

<!-- Profile -->
<section class="slide c3 r2">
  <header class="slide-head"><h2>MAIN HEADING</h2><p>Subheading goes here</p></header>
  <svg class="art" viewBox="0 0 255 144">
    <circle cx="50" cy="72" r="12" fill="#c9c9c9" role="img" aria-label="Profile portrait"/>
    <text x="50" y="92" text-anchor="middle" class="lb" style="font-size:3.6px">John Doe</text>
    <text x="50" y="96" text-anchor="middle" class="lbo" style="font-size:2.4px">CEO &amp; Founder</text>
    <g fill="var(--orange)"><circle cx="44" cy="101" r="1"/><circle cx="48" cy="101" r="1"/><circle cx="52" cy="101" r="1"/><circle cx="56" cy="101" r="1"/></g>
    <text x="90" y="50" class="lb" style="fill:#666">About</text>
    <text x="90" y="55" class="t">Add a short note about the</text><text x="90" y="58.5" class="t">person and their background.</text>
    <text x="90" y="66" class="lb" style="fill:#666">John</text>
    <text x="90" y="71" class="t">Add a short note about the</text><text x="90" y="74.5" class="t">work they lead each day.</text><text x="90" y="78" class="t">Keep it brief and clear.</text>
    <text x="90" y="85" class="t">One more line for a detail.</text>
    <text x="178" y="50" class="lb" style="fill:#666">Some Skill</text>
    <text x="178" y="55" class="t">Add a short skill note.</text>
    <rect x="178" y="61" width="68" height="1.6" fill="#ddd"/><rect x="178" y="61" width="58" height="1.6" fill="#3d7ec9"/>
    <rect x="178" y="69" width="68" height="1.6" fill="#ddd"/><rect x="178" y="69" width="32" height="1.6" fill="var(--orange)"/>
    <rect x="178" y="77" width="68" height="1.6" fill="#ddd"/><rect x="178" y="77" width="50" height="1.6" fill="var(--yellow)"/>
    <rect x="178" y="85" width="68" height="1.6" fill="#ddd"/><rect x="178" y="85" width="42" height="1.6" fill="var(--grey)"/>
  </svg>
  <div class="brand-foot"><i></i>Clear Ledger</div><span class="page-no">01</span>
</section>

<!-- Devices -->
<section class="slide c1 r3">
  <svg class="art" viewBox="0 0 255 144">
    <rect width="255" height="100" fill="var(--dark)"/>
    <text x="146" y="25" style="font-family:Montserrat,sans-serif;font-size:8.5px;font-weight:600;fill:var(--orange)">Devices <tspan fill="#fff">Mockup</tspan></text>
    <text x="146" y="30" class="t" style="fill:#bbb;font-size:2.2px">PUT YOUR GREAT SUBTITLE</text>
    <g class="t" style="fill:#ccc">
      <text x="146" y="38">» Add a short note about this point.</text>
      <text x="146" y="44">» Add one more detail worth a line.</text>
      <text x="146" y="50">» Keep each item brief.</text>
      <text x="146" y="56">» Close with a clear takeaway.</text>
    </g>
    <rect x="22" y="109" width="9" height="9" fill="var(--orange)"/><path d="M24.5 111 h4 v1.5 c0 2 -4 2 -4 0z M26.5 114 v2" stroke="#fff" stroke-width=".6" fill="none"/>
    <text x="34" y="112" class="lb" style="font-size:2.8px">Lorem ipsum</text><text x="34" y="116" class="t">Add a short note here.</text>
    <rect x="98" y="109" width="9" height="9" fill="var(--mid)"/><rect x="100.5" y="112.5" width="4" height="3.5" stroke="#fff" stroke-width=".6" fill="none"/>
    <text x="110" y="112" class="lb" style="font-size:2.8px">Lorem ipsum</text><text x="110" y="116" class="t">Add a short note here.</text>
    <rect x="175" y="109" width="9" height="9" fill="var(--yellow)"/><path d="M177 114 a3 3 0 0 1 5 0 M178.3 115.5 a1.3 1.3 0 0 1 2.4 0" stroke="#fff" stroke-width=".6" fill="none"/>
    <text x="187" y="112" class="lb" style="font-size:2.8px">Lorem ipsum</text><text x="187" y="116" class="t">Add a short note here.</text>
  </svg>
  <div class="photo" style="left:12px;top:12px;width:100px;height:72px;background:linear-gradient(160deg,#55585e,#46494e)" role="img" aria-label="Mockup of desktop monitor, laptop, tablet and phone"></div>
</section>

<!-- Ring diagram -->
<section class="slide c2 r3">
  <header class="slide-head"><h2>MAIN HEADING</h2><p>Subheading goes here</p></header>
  <svg class="art" viewBox="0 0 255 144">
    <g transform="translate(127 80) rotate(-90)" fill="none" stroke-width="11">
      <circle r="23" stroke="#3d3f44" stroke-dasharray="34 111"/>
      <circle r="23" stroke="#9a9a9a" stroke-dasharray="35 110" stroke-dashoffset="-36"/>
      <circle r="23" stroke="var(--orange)" stroke-dasharray="35 110" stroke-dashoffset="-72"/>
      <circle r="23" stroke="#f7c89a" stroke-dasharray="35 110" stroke-dashoffset="-108"/>
    </g>
    <circle cx="127" cy="80" r="15" fill="#fff" stroke="#e0e0e0" stroke-width="2"/>
    <text x="127" y="82" text-anchor="middle" class="num" style="font-size:5px;fill:#777">LOGO</text>
    <g class="num" style="font-size:4.6px;fill:#fff" text-anchor="middle">
      <text x="137" y="64">01</text><text x="147" y="98">02</text><text x="118" y="102">03</text><text x="105" y="68">04</text>
    </g>
    <text x="44" y="56" class="lb" style="font-size:2.8px">World Find</text><circle cx="79" cy="55" r="2.5" fill="none" stroke="var(--orange)" stroke-width=".6"/>
    <text x="40" y="61" class="t">Add a short note here.</text>
    <text x="44" y="104" class="lb" style="font-size:2.8px">Mail Letter</text><rect x="76" y="101" width="6" height="4" fill="none" stroke="#888" stroke-width=".6"/>
    <text x="40" y="109" class="t">Add a short note here.</text>
    <rect x="182" y="52" width="7" height="4.5" fill="none" stroke="#555" stroke-width=".6"/>
    <text x="195" y="56" class="lb" style="font-size:2.8px">Computer</text><text x="182" y="61" class="t">Add a short note here.</text>
    <path d="M182 101 h1.5 l1.5 4 h5 l1 -3 h-7" fill="none" stroke="#333" stroke-width=".6"/>
    <text x="195" y="105" class="lb" style="font-size:2.8px">Shoping</text><text x="182" y="110" class="t">Add a short note here.</text>
  </svg>
  <div class="brand-foot"><i></i>Clear Ledger</div><span class="page-no">01</span>
</section>

<!-- Pyramid -->
<section class="slide c3 r3">
  <header class="slide-head"><h2>MAIN HEADING</h2><p>Subheading goes here</p></header>
  <svg class="art" viewBox="0 0 255 144">
    <path d="M85 40 L79 52 H91Z" fill="#111"/>
    <path d="M78 55 H92 L99 68 H71Z" fill="#777"/>
    <path d="M70 71 H100 L107 84 H63Z" fill="#c5c5c5"/>
    <path d="M62 87 H108 L114 100 H56Z" fill="#f7c89a"/>
    <path d="M55 103 H115 L121 116 H49Z" fill="var(--orange)"/>
    <g text-anchor="middle" style="font-size:2.6px;fill:#fff"><text x="85" y="63">Step 1</text><text x="85" y="79">Step 2</text><text x="85" y="95">Step 3</text><text x="85" y="111">Step 4</text></g>
    <text x="158" y="46" class="lb" style="font-size:2.8px">STEP 1</text><text x="166" y="51" class="t">Add a short note here.</text>
    <text x="158" y="64" class="lb" style="font-size:2.8px">STEP 2</text><text x="166" y="69" class="t">Add a short note here.</text>
    <text x="158" y="82" class="lb" style="font-size:2.8px">STEP 3</text><text x="166" y="87" class="t">Add a short note here.</text>
    <text x="158" y="100" class="lb" style="font-size:2.8px">STEP 4</text><text x="166" y="105" class="t">Add a short note here.</text>
    <g fill="none" stroke="#444" stroke-width=".5"><circle cx="161" cy="50" r="1.8"/><circle cx="161" cy="68" r="1.8"/><circle cx="161" cy="86" r="1.8"/><circle cx="161" cy="104" r="1.8"/></g>
  </svg>
  <div class="brand-foot"><i></i>Clear Ledger</div><span class="page-no">01</span>
</section>

<!-- Road milestones -->
<section class="slide c1 r4">
  <header class="slide-head"><h2>MAIN HEADING</h2><p>Subheading goes here</p></header>
  <div class="photo" style="left:138px;top:16px;width:112px;height:112px;background:linear-gradient(160deg,#e6e6e6,#cfd0d2)" role="img" aria-label="Illustration of a winding road rising to the top right"></div>
  <svg class="art" viewBox="0 0 255 144">
    <g stroke="#999" stroke-width=".4"><line x1="158" y1="49" x2="158" y2="58"/><line x1="183" y1="37" x2="183" y2="48"/><line x1="205" y1="26" x2="205" y2="34"/><line x1="194" y1="82" x2="194" y2="110"/><line x1="226" y1="84" x2="226" y2="112"/></g>
    <g fill="#fff" stroke-width="1.4">
      <circle cx="205" cy="22" r="4" stroke="var(--dark)"/><circle cx="183" cy="32" r="5" stroke="#888"/><circle cx="158" cy="43" r="6" stroke="#aaa"/>
      <circle cx="194" cy="75" r="7" stroke="#f7c89a"/><circle cx="226" cy="75" r="9" stroke="var(--orange)"/>
    </g>
    <g class="num" text-anchor="middle">
      <text x="205" y="23.3" style="font-size:3.2px;fill:var(--dark)">01</text><text x="183" y="33.6" style="font-size:4px;fill:#888">02</text>
      <text x="158" y="45" style="font-size:5px;fill:#aaa">03</text><text x="194" y="77.5" style="font-size:6px;fill:#f7c89a">04</text>
      <text x="226" y="78.5" style="font-size:8px;fill:var(--orange)">05</text>
    </g>
    <text x="27" y="46" class="lb" style="font-size:2.8px">Lorem ipsum</text><text x="27" y="50" class="t">Add a short note here.</text>
    <text x="27" y="62" class="lb" style="font-size:2.8px">Lorem ipsum</text><text x="27" y="66" class="t">Add a short note here.</text>
    <text x="27" y="78" class="lb" style="font-size:2.8px">Lorem ipsum</text><text x="27" y="82" class="t">Add a short note here.</text>
    <text x="27" y="94" class="lb" style="font-size:2.8px">Lorem ipsum</text><text x="27" y="98" class="t">Add a short note here.</text>
    <text x="27" y="110" class="lb" style="font-size:2.8px">Lorem ipsum</text><text x="27" y="114" class="t">Add a short note here.</text>
  </svg>
  <div class="brand-foot"><i></i>Clear Ledger</div><span class="page-no">01</span>
</section>

<!-- Timeline -->
<section class="slide c2 r4">
  <header class="slide-head"><h2>MAIN HEADING</h2><p>Subheading goes here</p></header>
  <svg class="art" viewBox="0 0 255 144">
    <path d="M23 73 H62 L65 76.5 L62 80 H23Z" fill="var(--orange)"/>
    <path d="M65 73 H100 L103 76.5 L100 80 H65 L68 76.5Z" fill="#f3b378"/>
    <path d="M103 73 H138 L141 76.5 L138 80 H103 L106 76.5Z" fill="#9a9a9a"/>
    <path d="M141 73 H176 L179 76.5 L176 80 H141 L144 76.5Z" fill="#777"/>
    <path d="M179 73 H214 L217 76.5 L214 80 H179 L182 76.5Z" fill="#333"/>
    <path d="M217 73 H250 L250 80 H217 L220 76.5Z" fill="var(--orange)"/>
    <g text-anchor="middle" style="font-size:2.6px;fill:#fff">
      <text x="43" y="77.5">2010</text><text x="84" y="77.5">2011</text><text x="122" y="77.5">2012</text><text x="160" y="77.5">2013</text><text x="198" y="77.5">2014</text><text x="234" y="77.5">2015</text>
    </g>
    <g stroke="#888" stroke-width=".4"><line x1="43" y1="52" x2="43" y2="72"/><line x1="122" y1="52" x2="122" y2="72"/><line x1="198" y1="52" x2="198" y2="72"/><line x1="84" y1="81" x2="84" y2="102"/><line x1="160" y1="81" x2="160" y2="102"/><line x1="234" y1="81" x2="234" y2="102"/></g>
    <text x="20" y="45" class="lb" style="font-size:2.8px">Lorem 1</text><text x="20" y="49" class="t">Add a short note here.</text>
    <text x="98" y="45" class="lb" style="font-size:2.8px">Lorem 3</text><text x="98" y="49" class="t">Add a short note here.</text>
    <text x="176" y="45" class="lb" style="font-size:2.8px">Lorem 5</text><text x="176" y="49" class="t">Add a short note here.</text>
    <text x="60" y="108" class="lb" style="font-size:2.8px">Lorem 2</text><text x="60" y="112" class="t">Add a short note here.</text>
    <text x="138" y="108" class="lb" style="font-size:2.8px">Lorem 4</text><text x="138" y="112" class="t">Add a short note here.</text>
    <text x="212" y="108" class="lb" style="font-size:2.8px">Lorem 6</text><text x="212" y="112" class="t">Add a short note here.</text>
  </svg>
  <div class="brand-foot"><i></i>Clear Ledger</div><span class="page-no">01</span>
</section>

<!-- Map -->
<section class="slide c3 r4">
  <header class="slide-head"><h2>MAIN HEADING</h2><p>Subheading goes here</p></header>
  <div class="photo" style="left:26px;top:30px;width:214px;height:96px;background:#c4c4c4;border-radius:3px" role="img" aria-label="Grey world map with location markers"></div>
  <svg class="art" viewBox="0 0 255 144">
    <g fill="var(--dark)"><circle cx="48" cy="49" r="3"/><circle cx="81" cy="46" r="3"/><circle cx="98" cy="41" r="3"/><circle cx="113" cy="67" r="3.5"/><circle cx="98" cy="90" r="3"/><circle cx="98" cy="102" r="3"/></g>
    <g fill="var(--orange)"><circle cx="164" cy="54" r="3"/><circle cx="178" cy="62" r="3"/><circle cx="191" cy="50" r="3"/><circle cx="183" cy="72" r="3"/></g>
    <circle cx="211" cy="96" r="3" fill="#fff" stroke="#555" stroke-width=".6"/>
    <g stroke="var(--orange)" stroke-width=".5"><line x1="164" y1="45" x2="164" y2="51"/><line x1="183" y1="45" x2="183" y2="69"/></g>
    <rect x="20" y="60" width="90" height="13" rx="6.5" fill="var(--dark)"/>
    <text x="28" y="66" style="font-size:2.8px;fill:#fff;font-weight:700">Add a short note on this place</text>
    <text x="28" y="70" style="font-size:2.8px;fill:#fff;font-weight:700">and the people you reach.</text>
    <rect x="148" y="32" width="96" height="13" rx="6.5" fill="var(--orange)"/>
    <circle cx="154" cy="38.5" r="6.5" fill="var(--orange)" stroke="#fff" stroke-width=".8"/>
    <text x="163" y="38" style="font-size:2.8px;fill:#fff;font-weight:700">Add a short note on this place</text>
    <text x="163" y="42" style="font-size:2.8px;fill:#fff;font-weight:700">and the people you reach.</text>
    <rect x="130" y="110" width="96" height="13" rx="6.5" fill="#555"/>
    <circle cx="136" cy="116.5" r="6.5" fill="#555" stroke="#fff" stroke-width=".8"/>
    <text x="145" y="116" style="font-size:2.8px;fill:#fff;font-weight:700">Add a short note on this place</text>
    <text x="145" y="120" style="font-size:2.8px;fill:#fff;font-weight:700">and the people you reach.</text>
  </svg>
  <div class="brand-foot"><i></i>Clear Ledger</div><span class="page-no">01</span>
</section>

<!-- SWOT -->
<section class="slide c1 r5">
  <header class="slide-head"><h2>MAIN HEADING</h2><p>Subheading goes here</p></header>
  <svg class="art" viewBox="0 0 255 144">
    <g text-anchor="middle" style="font-size:4px;font-weight:700">
      <text x="47" y="45" fill="var(--orange)">STRENGTH</text><text x="100" y="45" fill="#999">WEAKNESS</text>
      <text x="153" y="45" fill="#555">OPPORTUNITY</text><text x="207" y="45" fill="#222">THREAT</text>
    </g>
    <rect x="22" y="48" width="50" height="74" fill="var(--orange)"/>
    <rect x="75" y="48" width="50" height="74" fill="#9a9a9a"/>
    <rect x="128" y="48" width="50" height="74" fill="#5e6064"/>
    <rect x="182" y="48" width="50" height="74" fill="#2f3135"/>
    <g style="font-size:2.4px;fill:#fff">
      <text x="26" y="56">• Add a short point.</text><text x="26" y="66">• Add a short point.</text><text x="26" y="76">• Add a short point.</text><text x="26" y="86">• Add a short point.</text>
      <text x="79" y="56">• Add a short point.</text><text x="79" y="66">• Add a short point.</text><text x="79" y="76">• Add a short point.</text><text x="79" y="86">• Add a short point.</text>
      <text x="132" y="56">• Add a short point.</text><text x="132" y="66">• Add a short point.</text><text x="132" y="76">• Add a short point.</text><text x="132" y="86">• Add a short point.</text>
      <text x="186" y="56">• Add a short point.</text><text x="186" y="66">• Add a short point.</text><text x="186" y="76">• Add a short point.</text><text x="186" y="86">• Add a short point.</text>
    </g>
  </svg>
  <div class="brand-foot"><i></i>Clear Ledger</div><span class="page-no">01</span>
</section>

<!-- Gender donut -->
<section class="slide c2 r5">
  <header class="slide-head"><h2>MAIN HEADING</h2><p>Subheading goes here</p></header>
  <svg class="art" viewBox="0 0 255 144">
    <g transform="translate(62 82) rotate(-90)" fill="none" stroke-width="9">
      <circle r="18" stroke="#555"/>
      <circle r="18" stroke="var(--orange)" stroke-dasharray="78 113"/>
    </g>
    <rect x="40" y="110" width="2" height="2" fill="#555"/><text x="43.5" y="112" style="font-size:2.8px;fill:#777">MALE</text>
    <rect x="55" y="110" width="2" height="2" fill="var(--orange)"/><text x="58.5" y="112" style="font-size:2.8px;fill:#777">FEMALE</text>
    <text x="135" y="47" style="font-size:3.8px;font-weight:700;fill:var(--orange)">GENDER ANALYSIS</text>
    <text x="135" y="52" style="font-size:2.8px;font-weight:700;fill:var(--orange)">Male Or Female?</text>
    <g class="t">
      <text x="135" y="57">Write a short paragraph here about the split and</text>
      <text x="135" y="61">what it means for the plan. Keep the words plain.</text>
      <text x="135" y="65">Add a second point to give the number context.</text>
      <text x="135" y="73">Use this space for a short follow up note on the</text>
      <text x="135" y="77">trend and the next step the team will take.</text>
      <text x="135" y="85">Close with one clear line that sums it all up.</text>
      <text x="135" y="89">Leave room so the slide stays light.</text>
    </g>
  </svg>
  <div class="brand-foot"><i></i>Clear Ledger</div><span class="page-no">01</span>
</section>

<!-- Two bar charts -->
<section class="slide c3 r5">
  <header class="slide-head"><h2>MAIN HEADING</h2><p>Subheading goes here</p></header>
  <svg class="art" viewBox="0 0 255 144">
    <g stroke="#bbb" stroke-width=".4"><line x1="16" y1="36" x2="16" y2="102"/><line x1="16" y1="102" x2="112" y2="102"/><line x1="140" y1="36" x2="140" y2="102"/><line x1="140" y1="102" x2="236" y2="102"/></g>
    <rect x="26" y="40" width="10" height="62" fill="var(--orange)"/><rect x="50" y="84" width="10" height="18" fill="#aaa"/><rect x="74" y="93" width="10" height="9" fill="#777"/><rect x="98" y="96" width="10" height="6" fill="#333"/>
    <rect x="150" y="40" width="10" height="62" fill="var(--orange)"/><rect x="174" y="72" width="10" height="30" fill="#aaa"/><rect x="198" y="82" width="10" height="20" fill="#777"/><rect x="222" y="76" width="10" height="26" fill="#333"/>
    <g style="font-size:1.8px;fill:#777"><text x="20" y="106">■ DESIGNING ■ MARKETING ■ ACCOUNTING ■ PHOTOGRAPHY</text><text x="144" y="106">■ DESIGNING ■ MARKETING ■ ACCOUNTING ■ PHOTOGRAPHY</text></g>
    <text x="17" y="122" class="num" style="font-size:14px;fill:var(--orange)">70%</text>
    <text x="140" y="122" class="num" style="font-size:14px;fill:#555">45%</text>
    <g class="t"><text x="58" y="114">Add a short note about</text><text x="58" y="118">this result and its cause.</text><text x="182" y="114">Add a short note about</text><text x="182" y="118">this result and its cause.</text></g>
  </svg>
  <div class="brand-foot"><i></i>Clear Ledger</div><span class="page-no">01</span>
</section>

<!-- Four donuts -->
<section class="slide c1 r6">
  <header class="slide-head"><h2>MAIN HEADING</h2><p>Subheading goes here</p></header>
  <svg class="art" viewBox="0 0 255 144">
    <g fill="none" stroke-width="6">
      <g transform="translate(50 66) rotate(-90)"><circle r="17" stroke="#ddd"/><circle r="17" stroke="var(--orange)" stroke-dasharray="75 107"/></g>
      <g transform="translate(103 66) rotate(-90)"><circle r="17" stroke="#ddd"/><circle r="17" stroke="#8a8a8a" stroke-dasharray="53 107"/></g>
      <g transform="translate(156 66) rotate(-90)"><circle r="17" stroke="#ddd"/><circle r="17" stroke="var(--yellow)" stroke-dasharray="48 107"/></g>
      <g transform="translate(209 66) rotate(-90)"><circle r="17" stroke="#ddd"/><circle r="17" stroke="#2f3135" stroke-dasharray="96 107"/></g>
    </g>
    <g text-anchor="middle" style="font-size:6px;fill:#555"><text x="50" y="68">70%</text><text x="103" y="68">50%</text><text x="156" y="68">45%</text><text x="209" y="68">90%</text></g>
    <g class="t">
      <text x="28" y="96">Write a short paragraph here that explains what the four numbers show and why they matter to the team.</text>
      <text x="28" y="100">Keep each line brief and plain so the slide reads well from the back of the room and stays clean.</text>
      <text x="28" y="104">Add one more line for a detail, then a closing thought to wrap up the point.</text>
    </g>
  </svg>
  <div class="brand-foot"><i></i>Clear Ledger</div><span class="page-no">01</span>
</section>

<!-- 2014 / 2015 -->
<section class="slide c2 r6">
  <header class="slide-head"><h2>MAIN HEADING</h2><p>Subheading goes here</p></header>
  <svg class="art" viewBox="0 0 255 144">
    <circle cx="71" cy="70" r="26" fill="#e4e4e4"/>
    <g transform="translate(71 70) rotate(-90)" fill="none" stroke-width="4">
      <circle r="20" stroke="var(--orange)" stroke-dasharray="19 126"/>
      <circle r="20" stroke="var(--yellow)" stroke-dasharray="24 126" stroke-dashoffset="-20"/>
      <circle r="20" stroke="#aaa" stroke-dasharray="62 126" stroke-dashoffset="-45"/>
      <circle r="20" stroke="#222" stroke-dasharray="18 126" stroke-dashoffset="-108"/>
    </g>
    <circle cx="71" cy="70" r="16" fill="#fff"/>
    <text x="71" y="73" text-anchor="middle" class="num" style="font-size:8px;fill:#333">2014</text>
    <circle cx="185" cy="70" r="26" fill="#e4e4e4"/>
    <g transform="translate(185 70) rotate(-90)" fill="none" stroke-width="4">
      <circle r="20" stroke="var(--orange)" stroke-dasharray="30 126"/>
      <circle r="20" stroke="#aaa" stroke-dasharray="32 126" stroke-dashoffset="-31"/>
      <circle r="20" stroke="#222" stroke-dasharray="20 126" stroke-dashoffset="-64"/>
      <circle r="20" stroke="var(--yellow)" stroke-dasharray="40 126" stroke-dashoffset="-85"/>
    </g>
    <circle cx="185" cy="70" r="16" fill="#fff"/>
    <text x="185" y="73" text-anchor="middle" class="num" style="font-size:8px;fill:#333">2015</text>
    <g style="font-size:2px;fill:#fff;font-weight:700" text-anchor="middle">
      <circle cx="78" cy="42" r="3" fill="var(--orange)"/><text x="78" y="42.8">15%</text>
      <circle cx="47" cy="57" r="3" fill="var(--yellow)"/><text x="47" y="57.8">17%</text>
      <circle cx="98" cy="78" r="3" fill="#aaa"/><text x="98" y="78.8">41%</text>
      <circle cx="51" cy="92" r="3" fill="#222"/><text x="51" y="92.8">28%</text>
      <circle cx="174" cy="42" r="3" fill="var(--orange)"/><text x="174" y="42.8">27%</text>
      <circle cx="212" cy="57" r="3" fill="#aaa"/><text x="212" y="57.8">24%</text>
      <circle cx="212" cy="88" r="3" fill="#222"/><text x="212" y="88.8">16%</text>
      <circle cx="160" cy="92" r="3" fill="var(--yellow)"/><text x="160" y="92.8">33%</text>
    </g>
    <g style="font-size:2.8px;fill:#666">
      <circle cx="64" cy="111" r="1" fill="var(--orange)"/><text x="66" y="112">Lorem</text>
      <circle cx="104" cy="111" r="1" fill="var(--yellow)"/><text x="106" y="112">Lorem</text>
      <circle cx="144" cy="111" r="1" fill="#aaa"/><text x="146" y="112">Lorem</text>
      <circle cx="184" cy="111" r="1" fill="#222"/><text x="186" y="112">Lorem</text>
    </g>
  </svg>
  <div class="brand-foot"><i></i>Clear Ledger</div><span class="page-no">01</span>
</section>

<!-- Humps -->
<section class="slide c3 r6">
  <header class="slide-head"><h2>MAIN HEADING</h2><p>Subheading goes here</p></header>
  <svg class="art" viewBox="0 0 255 144">
    <path d="M18 86 C22 60 38 60 42 86Z" fill="#555"/>
    <path d="M32 86 C38 52 54 52 58 86Z" fill="var(--orange)"/>
    <path d="M50 86 C56 58 72 58 78 86Z" fill="#aaa"/>
    <path d="M68 86 C74 50 92 50 98 86Z" fill="var(--yellow)"/>
    <path d="M88 86 C94 56 110 56 116 86Z" fill="#777"/>
    <path d="M106 86 C112 50 130 50 136 86Z" fill="var(--orange)"/>
    <path d="M126 86 C132 58 148 58 154 86Z" fill="#888"/>
    <path d="M144 86 C150 50 168 50 174 86Z" fill="#555"/>
    <path d="M164 86 C170 58 186 58 192 86Z" fill="var(--yellow)"/>
    <path d="M182 86 C188 50 206 50 212 86Z" fill="#888"/>
    <path d="M202 86 C208 56 226 56 236 86Z" fill="var(--yellow)"/>
    <g stroke-width=".4">
      <line x1="30" y1="49" x2="30" y2="66" stroke="#555"/><line x1="45" y1="43" x2="45" y2="56" stroke="#555"/><line x1="64" y1="48" x2="64" y2="62" stroke="#555"/><line x1="83" y1="40" x2="83" y2="54" stroke="#555"/><line x1="102" y1="46" x2="102" y2="60" stroke="#555"/><line x1="121" y1="40" x2="121" y2="54" stroke="#555"/><line x1="140" y1="48" x2="140" y2="62" stroke="#555"/><line x1="159" y1="40" x2="159" y2="54" stroke="#555"/><line x1="178" y1="48" x2="178" y2="62" stroke="#555"/><line x1="197" y1="40" x2="197" y2="54" stroke="#555"/><line x1="219" y1="46" x2="219" y2="60" stroke="#555"/>
    </g>
    <circle cx="30" cy="49" r="3" fill="#555"/><circle cx="45" cy="43" r="3" fill="var(--orange)"/><circle cx="64" cy="48" r="3" fill="#aaa"/><circle cx="83" cy="40" r="3" fill="var(--yellow)"/>
    <circle cx="102" cy="46" r="3" fill="#777"/><circle cx="121" cy="40" r="3" fill="var(--orange)"/><circle cx="140" cy="48" r="3" fill="#6fa83b"/>
    <circle cx="159" cy="40" r="3" fill="#555"/><circle cx="178" cy="48" r="3" fill="var(--yellow)"/><circle cx="197" cy="40" r="3" fill="#888"/><circle cx="219" cy="46" r="3" fill="var(--orange)"/>
    <g fill="#fff"><circle cx="30" cy="49" r="1.2"/><circle cx="45" cy="43" r="1.2"/><circle cx="64" cy="48" r="1.2"/><circle cx="83" cy="40" r="1.2"/><circle cx="102" cy="46" r="1.2"/><circle cx="121" cy="40" r="1.2"/><circle cx="140" cy="48" r="1.2"/><circle cx="159" cy="40" r="1.2"/><circle cx="178" cy="48" r="1.2"/><circle cx="197" cy="40" r="1.2"/><circle cx="219" cy="46" r="1.2"/></g>
    <text x="18" y="104" style="font-size:6px;fill:#444">Lorem ipsum</text>
    <g class="t"><text x="18" y="109">Write a short paragraph here that explains the chart and the trend it shows to the audience, in plain words.</text>
      <text x="18" y="113">Add one more line for a detail worth noting and keep the rest of the slide open.</text></g>
  </svg>
  <div class="brand-foot"><i></i>Clear Ledger</div><span class="page-no">01</span>
</section>

<!-- Area chart -->
<section class="slide c1 r7">
  <header class="slide-head"><h2>MAIN HEADING</h2><p>Subheading goes here</p></header>
  <svg class="art" viewBox="0 0 255 144">
    <g stroke="#ddd" stroke-width=".3"><line x1="14" y1="36" x2="128" y2="36"/><line x1="14" y1="48" x2="128" y2="48"/><line x1="14" y1="60" x2="128" y2="60"/><line x1="14" y1="72" x2="128" y2="72"/><line x1="14" y1="84" x2="128" y2="84"/></g>
    <path d="M14 84 L14 58 L40 48 L60 54 L84 44 L108 52 L128 42 L128 84Z" fill="var(--orange)"/>
    <path d="M14 84 L14 62 L40 56 L60 66 L84 50 L108 60 L128 52 L128 84Z" fill="#aaa"/>
    <path d="M14 84 L14 76 L40 72 L60 70 L84 68 L108 74 L128 62 L128 84Z" fill="#555"/>
    <g style="font-size:2px;fill:#999"><text x="14" y="88">$1,000</text><text x="38" y="88">$2,000</text><text x="62" y="88">$3,000</text><text x="86" y="88">$4,000</text><text x="110" y="88">$5,000</text></g>
    <path d="M23 100 h4 v1.5 c0 2 -4 2 -4 0z M25 103 v2 M23.5 105 h3" stroke="var(--orange)" stroke-width=".7" fill="none"/>
    <g class="t"><text x="32" y="101">Add a short note about the chart</text><text x="32" y="104.5">and the trend it shows in plain</text><text x="32" y="108">words for the room.</text></g>
    <circle cx="152" cy="58" r="5" fill="var(--orange)"/><rect x="150" y="56" width="4" height="4" fill="none" stroke="#fff" stroke-width=".5"/>
    <circle cx="152" cy="80" r="5" fill="#aaa"/><path d="M150 80 l1.5 1.5 l3 -3" stroke="#fff" stroke-width=".6" fill="none"/>
    <circle cx="152" cy="102" r="5" fill="#333"/><rect x="150" y="100.5" width="4" height="3" fill="none" stroke="#fff" stroke-width=".5"/>
    <text x="162" y="56" style="font-size:3.6px;fill:#555">Lorem ipsum</text><text x="162" y="61" class="t">Add a short note here.</text><text x="162" y="64.5" class="t">Keep the line brief.</text>
    <text x="162" y="78" style="font-size:3.6px;fill:#555">Lorem ipsum</text><text x="162" y="83" class="t">Add a short note here.</text><text x="162" y="86.5" class="t">Keep the line brief.</text>
    <text x="162" y="100" style="font-size:3.6px;fill:#555">Lorem ipsum</text><text x="162" y="105" class="t">Add a short note here.</text><text x="162" y="108.5" class="t">Keep the line brief.</text>
  </svg>
  <div class="brand-foot"><i></i>Clear Ledger</div><span class="page-no">01</span>
</section>

<!-- Stacked bar groups -->
<section class="slide c2 r7">
  <header class="slide-head"><h2>MAIN HEADING</h2><p>Subheading goes here</p></header>
  <svg class="art" viewBox="0 0 255 144">
    <defs>
      <g id="stackA"><rect width="4" height="8" fill="#333"/><rect y="8" width="4" height="14" fill="#aaa"/><rect y="22" width="4" height="20" fill="var(--orange)"/></g>
      <g id="stackB"><rect width="4" height="14" fill="#333"/><rect y="14" width="4" height="10" fill="#aaa"/><rect y="24" width="4" height="18" fill="var(--orange)"/></g>
      <g id="barGroup">
        <line x1="-4" y1="0" x2="-4" y2="42" stroke="#ccc" stroke-width=".3"/>
        <use href="#stackA"/><use href="#stackB" x="7"/><use href="#stackA" x="14"/><use href="#stackB" x="21"/>
        <line x1="-4" y1="42" x2="27" y2="42" stroke="#ccc" stroke-width=".3"/>
      </g>
    </defs>
    <use href="#barGroup" x="34" y="47"/>
    <use href="#barGroup" x="118" y="47"/>
    <use href="#barGroup" x="203" y="47"/>
    <text x="20" y="107" style="font-size:3.2px;fill:#555">Lorem</text><text x="20" y="111" class="t">Add a short note here.</text><text x="20" y="114.5" class="t">Keep the line brief.</text>
    <text x="104" y="107" style="font-size:3.2px;fill:#555">Lorem</text><text x="104" y="111" class="t">Add a short note here.</text><text x="104" y="114.5" class="t">Keep the line brief.</text>
    <text x="189" y="107" style="font-size:3.2px;fill:#555">Lorem</text><text x="189" y="111" class="t">Add a short note here.</text><text x="189" y="114.5" class="t">Keep the line brief.</text>
  </svg>
  <div class="brand-foot"><i></i>Clear Ledger</div><span class="page-no">01</span>
</section>

<!-- Wide stacked bars -->
<section class="slide c3 r7">
  <header class="slide-head"><h2>MAIN HEADING</h2><p>Subheading goes here</p></header>
  <svg class="art" viewBox="0 0 255 144">
    <g class="t"><text x="16" y="30">Write a short paragraph here that sets up the chart below and tells the audience what to look for first.</text>
      <text x="16" y="34">Keep it to two lines so the chart has room to breathe.</text></g>
    <g stroke="#ddd" stroke-width=".3"><line x1="22" y1="46" x2="222" y2="46"/><line x1="22" y1="58" x2="222" y2="58"/><line x1="22" y1="70" x2="222" y2="70"/><line x1="22" y1="82" x2="222" y2="82"/><line x1="22" y1="94" x2="222" y2="94"/></g>
    <rect x="40" y="46" width="14" height="6" fill="#333"/><rect x="40" y="52" width="14" height="20" fill="#aaa"/><rect x="40" y="72" width="14" height="22" fill="var(--orange)"/>
    <rect x="88" y="46" width="14" height="10" fill="#333"/><rect x="88" y="56" width="14" height="16" fill="#aaa"/><rect x="88" y="72" width="14" height="22" fill="var(--orange)"/>
    <rect x="136" y="46" width="14" height="8" fill="#333"/><rect x="136" y="54" width="14" height="18" fill="#aaa"/><rect x="136" y="72" width="14" height="22" fill="var(--orange)"/>
    <rect x="184" y="46" width="14" height="8" fill="#333"/><rect x="184" y="54" width="14" height="14" fill="#aaa"/><rect x="184" y="68" width="14" height="26" fill="var(--orange)"/>
    <g style="font-size:2px;fill:#777"><rect x="226" y="60" width="2" height="2" fill="#333"/><text x="229" y="62">Lorem</text><rect x="226" y="66" width="2" height="2" fill="#aaa"/><text x="229" y="68">Lorem</text><rect x="226" y="72" width="2" height="2" fill="var(--orange)"/><text x="229" y="74">Lorem</text></g>
    <text x="16" y="107" style="font-size:3.2px;fill:#555">Lorem</text><text x="16" y="111" class="t">Add a short note here.</text><text x="16" y="114.5" class="t">Keep the line brief.</text>
    <text x="96" y="107" style="font-size:3.2px;fill:#555">Lorem</text><text x="96" y="111" class="t">Add a short note here.</text><text x="96" y="114.5" class="t">Keep the line brief.</text>
    <text x="173" y="107" style="font-size:3.2px;fill:#555">Lorem</text><text x="173" y="111" class="t">Add a short note here.</text><text x="173" y="114.5" class="t">Keep the line brief.</text>
  </svg>
  <div class="brand-foot"><i></i>Clear Ledger</div><span class="page-no">01</span>
</section>

<!-- Line chart -->
<section class="slide c1 r8">
  <header class="slide-head"><h2>MAIN HEADING</h2><p>Subheading goes here</p></header>
  <svg class="art" viewBox="0 0 255 144">
    <g stroke="#ddd" stroke-width=".3"><line x1="24" y1="40" x2="232" y2="40"/><line x1="24" y1="52" x2="232" y2="52"/><line x1="24" y1="64" x2="232" y2="64"/><line x1="24" y1="76" x2="232" y2="76"/><line x1="24" y1="88" x2="232" y2="88"/></g>
    <polyline points="38,70 78,58 118,68 158,38 198,60 218,58" fill="none" stroke="#555" stroke-width=".6"/>
    <polyline points="38,64 78,66 118,62 158,72 198,66 218,64" fill="none" stroke="var(--orange)" stroke-width=".6"/>
    <polyline points="38,74 78,70 118,64 158,62 198,68 218,70" fill="none" stroke="var(--yellow)" stroke-width=".6"/>
    <polyline points="38,68 78,74 118,72 158,66 198,64 218,66" fill="none" stroke="#aaa" stroke-width=".6"/>
    <g style="font-size:2px;fill:#999"><text x="34" y="92">$1,000</text><text x="74" y="92">$2,000</text><text x="114" y="92">$3,000</text><text x="154" y="92">$4,000</text><text x="194" y="92">$5,000</text></g>
    <g style="font-size:2.2px;fill:#777"><rect x="96" y="96" width="4" height="1" fill="#555"/><text x="101" y="97.5">Lorem</text><rect x="114" y="96" width="4" height="1" fill="var(--orange)"/><text x="119" y="97.5">Lorem</text><rect x="132" y="96" width="4" height="1" fill="var(--yellow)"/><text x="137" y="97.5">Lorem</text><rect x="150" y="96" width="4" height="1" fill="#aaa"/><text x="155" y="97.5">Lorem</text></g>
    <g class="t" text-anchor="middle">
      <text x="40" y="112">Lorem ipsum</text><text x="40" y="116">Short note here.</text>
      <text x="80" y="112">Lorem ipsum</text><text x="80" y="116">Short note here.</text>
      <text x="120" y="112">Lorem ipsum</text><text x="120" y="116">Short note here.</text>
      <text x="160" y="112">Lorem ipsum</text><text x="160" y="116">Short note here.</text>
      <text x="200" y="112">Lorem ipsum</text><text x="200" y="116">Short note here.</text>
    </g>
  </svg>
  <div class="brand-foot"><i></i>Clear Ledger</div><span class="page-no">01</span>
</section>

<!-- Grouped bars -->
<section class="slide c2 r8">
  <header class="slide-head"><h2>MAIN HEADING</h2><p>Subheading goes here</p></header>
  <svg class="art" viewBox="0 0 255 144">
    <g stroke="#ddd" stroke-width=".3"><line x1="24" y1="40" x2="232" y2="40"/><line x1="24" y1="52" x2="232" y2="52"/><line x1="24" y1="64" x2="232" y2="64"/><line x1="24" y1="76" x2="232" y2="76"/><line x1="24" y1="88" x2="232" y2="88"/></g>
    <rect x="28" y="64" width="6" height="24" fill="var(--orange)"/><rect x="35" y="70" width="6" height="18" fill="#aaa"/><rect x="42" y="76" width="6" height="12" fill="#555"/>
    <rect x="68" y="64" width="6" height="24" fill="var(--orange)"/><rect x="75" y="66" width="6" height="22" fill="#aaa"/><rect x="82" y="74" width="6" height="14" fill="#555"/>
    <rect x="108" y="70" width="6" height="18" fill="var(--orange)"/><rect x="115" y="68" width="6" height="20" fill="#aaa"/><rect x="122" y="46" width="6" height="42" fill="#555"/>
    <rect x="148" y="70" width="6" height="18" fill="var(--orange)"/><rect x="155" y="62" width="6" height="26" fill="#aaa"/><rect x="162" y="74" width="6" height="14" fill="#555"/>
    <rect x="188" y="66" width="6" height="22" fill="var(--orange)"/><rect x="195" y="54" width="6" height="34" fill="#aaa"/><rect x="202" y="64" width="6" height="24" fill="#555"/>
    <g style="font-size:2px;fill:#999"><text x="32" y="92">Item</text><text x="72" y="92">Item</text><text x="112" y="92">Item</text><text x="152" y="92">Item</text><text x="192" y="92">Item</text></g>
    <g style="font-size:2.2px;fill:#777"><rect x="100" y="96" width="2" height="2" fill="var(--orange)"/><text x="103" y="97.8">Lorem</text><rect x="118" y="96" width="2" height="2" fill="#aaa"/><text x="121" y="97.8">Lorem</text><rect x="136" y="96" width="2" height="2" fill="#555"/><text x="139" y="97.8">Lorem</text></g>
    <g class="t" text-anchor="middle">
      <text x="40" y="112">Lorem ipsum</text><text x="40" y="116">Short note here.</text>
      <text x="80" y="112">Lorem ipsum</text><text x="80" y="116">Short note here.</text>
      <text x="120" y="112">Lorem ipsum</text><text x="120" y="116">Short note here.</text>
      <text x="160" y="112">Lorem ipsum</text><text x="160" y="116">Short note here.</text>
      <text x="200" y="112">Lorem ipsum</text><text x="200" y="116">Short note here.</text>
    </g>
  </svg>
  <div class="brand-foot"><i></i>Clear Ledger</div><span class="page-no">01</span>
</section>

<!-- Thank you -->
<section class="slide c3 r8 thanks">
  <h2>THANK YOU FOR YOUR TIME</h2>
  <svg class="art" viewBox="0 0 255 144">
    <g fill="#fff"><circle cx="21" cy="88" r="3"/><circle cx="21" cy="97" r="3"/><circle cx="21" cy="106" r="3"/><circle cx="21" cy="115" r="3"/></g>
    <g fill="none" stroke="var(--orange)" stroke-width=".6">
      <path d="M19.8 86.8 c0 2 1.4 3.4 2.4 2.4"/>
      <path d="M21 98.8 c-1.5 -1.6 -1.5 -3 0 -3 c1.5 0 1.5 1.4 0 3z"/>
      <rect x="19.5" y="105" width="3" height="2"/>
      <circle cx="21" cy="115" r="1.3"/>
    </g>
    <g style="font-size:2.2px;fill:#fff"><text x="28" y="88.8">Phone</text><text x="28" y="97.8">Office</text><text x="28" y="106.8">Mail</text><text x="28" y="115.8">Web</text></g>
  </svg>
</section>

</main>
</body>
</html>
```